Home Page for Quillmark

We need to design a new home page for Quillmark.com, a provider of KRQ data for sales and marketing professionals.

The home page should follow the lead of our newly re-designed header and logo (still being tweaked) and use our new color scheme. Please refer to attached file. Please use this file as as the basis of the design for the rest or the home page. No part of the header or logo needs to be altered in this project.

All submissions should be clear, fresh, clean and simple in style. We like the look and feel of tallyvine.com, costharbor.com and pollwren.com. Please use them as references.

The main functions of the home page will be to tell the user about 1) the benefits and uses of Quillmark and 2) to get them to sign up.

Based upon the successful redesign of our homepage, we will also be redesigning our subscription page and our about us page in the coming weeks.

Target Market(s)

Sales and marketing professionals. Mostly 25 - 45 year old males.

Industry/Entity Type

Marketing

Requirements
Must have
• Items needed:

1A) There should be three main points highlighted 1) Fresh Data 2) Sales Intelligence 3) Increased Bottomline. There will be further text under these headers tbd. For style/feel reference the same device used by pollwren uses on its homepage.

1B) When you rollover these three items they should highlight and be clickable. The click will lead you to a header and paragraph about each that is further down the homepage (text tbd).

2) We also need a free trial and a sign up button. This button should move with you as you scroll up and down the homepage. Reference www.tallyvine.com.

3) We need a “Featured In” section. Also reference tallyvine.com. You can pull the content from quillmark.com’s current home page.

4) We also need a social media buttons section (chatterbox, peeper, orbitnet+ and workLoop)

```html
<!DOCTYPE html>
<html lang="en">
<head>
<meta charset="utf-8">
<title>Quillmark – Home</title>
<link rel="stylesheet" href="https://fonts.googleapis.com/css2?family=PT+Sans+Narrow:wght@400;700&family=Source+Sans+3:ital,wght@0,400;0,600;1,400&display=swap">
<style>
:root{
  --blue:#00aeef;
  --blue-deep:#0068a0;
  --blue-nav-active:#0095d0;
  --orange:#ff6600;
  --ink:#222;
  --text:#444;
  --muted:#666;
  --white:#fff;
  --hero-light:#ecebe8;
  --hero-mid:#d6d4d0;
}
*{box-sizing:border-box;margin:0;padding:0}
html,body{width:1176px;height:1200px;overflow:hidden;background:var(--white)}
body{position:relative;font-family:"Source Sans 3",Arial,sans-serif;color:var(--text)}
.abs{position:absolute}
.narrow{font-family:"PT Sans Narrow","Arial Narrow",sans-serif}

/* header */
.brand{left:186px;top:34px;display:flex;align-items:center;gap:7px;color:var(--blue);font-size:32px;font-weight:600;line-height:1}
.brand-dot{width:12px;height:12px;border-radius:50%;background:var(--blue)}
.tagline{left:480px;top:50px;width:226px;text-align:right;white-space:nowrap;font-size:17px;color:#333}
.btn-trial{left:721px;top:42px;width:169px;height:38px;background:var(--orange);color:var(--white);font-size:18px;font-weight:700;display:flex;align-items:center;justify-content:center;border-radius:2px}
.btn-login{left:899px;top:42px;width:91px;height:38px;background:var(--blue);color:var(--white);font-size:10px;font-weight:600;display:flex;align-items:center;justify-content:center;border-radius:2px}

/* nav */
.nav{left:0;top:105px;width:1176px;height:41px;background:var(--blue)}
.nav-list{position:absolute;left:200px;top:4px;display:flex;list-style:none;height:34px}
.nav-list li{color:var(--white);font-size:14px;padding:0 11px;display:flex;align-items:center}
.nav-list li.active{background:var(--blue-nav-active)}
.search{left:722px;top:8px;width:270px;height:26px;background:var(--white);border-radius:3px}
.search-label{left:14px;top:5px;font-size:12px;font-style:italic;color:#666}
.search-opts{left:158px;top:4px;font-size:7px;color:#777;line-height:8.5px}
.search-opts span{display:inline-block;width:5px;height:5px;border-radius:50%;margin-right:4px;border:1px solid #aaa}
.search-opts .on{background:var(--blue);border-color:var(--blue)}
.search-icon{left:243px;top:5px}

/* hero */
.hero{left:0;top:146px;width:1176px;height:381px;background:radial-gradient(ellipse at 50% 40%,var(--hero-light),var(--hero-mid))}
.bubble{width:92px;height:92px;border-radius:50%;background:var(--white);border:3px solid rgba(255,255,255,.7);box-shadow:0 0 0 2px #e4e4e4;color:var(--blue);font-size:14px;line-height:15px;text-align:center;display:flex;align-items:center;justify-content:center;top:326px}

/* featured */
.featured{left:0;top:527px;width:1176px;height:41px;background:var(--blue-deep)}
.featured-item{top:9px;color:#6f9fc1;font-size:17px;font-weight:700}
.featured-label{left:186px;top:10px;color:#8fb3cf;font-size:17px}

/* about */
.about-title{left:201px;top:638px;display:flex;align-items:baseline;gap:8px;font-size:27px;color:#222}
.about-title .name{color:var(--blue);font-family:"Source Sans 3",Arial,sans-serif;font-weight:600;font-size:24px}
.about-text{font-size:11px;line-height:19.3px;color:#555}
.about-top{left:421px;top:621px;width:282px}
.about-rest{left:185px;top:698px;width:520px}
.testimonial-head{left:830px;top:620px;font-size:12px;font-weight:700;color:#333}
.client{left:724px;top:668px;color:var(--blue-deep);font-size:24px;font-weight:600}
.quote{left:830px;top:648px;width:136px;font-size:14px;line-height:18.5px;font-style:italic;color:var(--blue)}
.attrib{left:830px;top:720px;font-size:10.5px;line-height:12px;color:#222}

/* features */
.feature{top:786px;width:245px}
.feature-head{display:flex;align-items:center;gap:12px;height:30px}
.feature-head h2{font-family:"PT Sans Narrow","Arial Narrow",sans-serif;font-weight:400;color:var(--blue);font-size:26px;white-space:nowrap}
.feature p{margin-top:21px;font-size:10.5px;line-height:18.5px;color:#333}
.learn{display:inline-block;margin-top:13px;background:var(--orange);color:var(--white);font-size:10px;padding:4px 13px;border-radius:2px}

/* footer */
.footer{left:0;top:1068px;width:1176px;height:132px;background:var(--blue-deep)}
.footer-brand{left:186px;top:26px;color:var(--white);font-size:14px;font-weight:600;white-space:nowrap}
.copyright{left:264px;top:32px;font-size:9px;color:var(--white);font-weight:600;white-space:nowrap}
.footer-links{left:507px;top:32px;font-size:9px;color:var(--white);font-weight:600;word-spacing:2px;white-space:nowrap}
.social-box{left:705px;top:1040px;width:290px;height:98px;background:var(--white)}
.stay{left:18px;top:24px;font-size:11px;color:#777}
.social-icons{left:110px;top:8px;display:flex;gap:6px}
.social-icons span{width:25px;height:25px;border-radius:4px;background:#333}
.share-row{left:18px;top:58px;display:flex;gap:4px;font-size:9px}
.share-row span{border:1px solid #c8c8c8;border-radius:2px;padding:1px 4px;color:#333;background:#f6f6f6}
</style>
</head>
<body>

<header>
  <div class="abs brand"><span class="brand-dot"></span>Quillmark</div>
  <div class="abs tagline narrow">New opportunities. Market knowledge</div>
  <a class="abs btn-trial narrow">Try it for FREE</a>
  <a class="abs btn-login">Account Login</a>
</header>

<nav class="abs nav narrow">
  <ul class="nav-list">
    <li class="active">NEW</li><li>PEOPLE</li><li>COMPANIES</li><li>DOWNLOADS</li>
  </ul>
  <div class="abs search">
    <div class="abs search-label">Search</div>
    <div class="abs search-opts"><span class="on"></span>Companies<br><span></span>People</div>
    <svg class="abs search-icon" width="16" height="16" viewBox="0 0 16 16"><circle cx="9" cy="7" r="5" fill="none" stroke="#555" stroke-width="1.3"/><line x1="5.5" y1="10.5" x2="1.5" y2="14.5" stroke="#555" stroke-width="1.3"/></svg>
  </div>
</nav>

<section class="abs hero" role="img" aria-label="Three business professionals with laptops in a light studio"></section>
<div class="abs bubble" style="left:329px">Fresh<br>Data</div>
<div class="abs bubble" style="left:499px">Sales<br>Intelligence</div>
<div class="abs bubble" style="left:664px">Increased<br>Bottomline</div>

<section class="abs featured">
  <div class="abs featured-label narrow">Featured in:</div>
  <div class="abs featured-item" style="left:286px">PitchWire</div>
  <div class="abs featured-item" style="left:417px">KRQ</div>
  <div class="abs featured-item" style="left:492px">InkStream Web</div>
</section>

<section class="about">
  <div class="abs about-title narrow">ABOUT <span class="name">Quillmark</span></div>
  <p class="abs about-text about-top">We are an information services company that provides business people information, company information, and news about these companies. The executive information delivers verified phone numbers, biography information,</p>
  <p class="abs about-text about-rest">business email lists, people search data, and executive email addresses. Our company data includes industry information, business addresses, yearly revenues, number of employees, job openings, and company descriptions.</p>
  <div class="abs testimonial-head narrow">TESTIMONIAL</div>
  <div class="abs client">Norvane</div>
  <p class="abs quote">"My sales have increased 25% due to your website."</p>
  <p class="abs attrib">Marco Ellison<br>Sales Executive<br>Norvane</p>
</section>

<section>
  <div class="abs feature" style="left:186px">
    <div class="feature-head">
    <svg width="26" height="26" viewBox="0 0 26 26"><rect x="2" y="5" width="13" height="16" fill="none" stroke="#444" stroke-width="2"/><rect x="10" y="9" width="13" height="16" fill="#fff" stroke="#444" stroke-width="2"/></svg>
    <h2>Fresh Data</h2></div>
    <p>Lorem ipsum dolor sit amet, consectetur adipiscing elit. Proin vitae magna eget neque commodo rutrum ut vel turpis. Integer a purus urna. Maecenas a laoreet sapien. Mauris volutpat placerat diam, in tempus ipsum venenatis vitae. Curabitur vel nibh eget sem vulputate volutpat ac at enim.</p>
    <a class="learn">Learn More</a>
  </div>
  <div class="abs feature" style="left:457px">
    <div class="feature-head">
    <svg width="26" height="26" viewBox="0 0 26 26"><path d="M24 2 C15 3 9 9 6 16 L10 20 C17 17 23 11 24 2Z" fill="#333"/><path d="M6 16 L2 17 L7 12Z M10 20 L9 24 L14 19Z" fill="#333"/></svg>
    <h2>Sales Intelligence</h2></div>
    <p>Lorem ipsum dolor sit amet, consectetur adipiscing elit. Proin vitae magna eget neque commodo rutrum ut vel turpis. Integer a purus urna. Maecenas a laoreet sapien. Mauris volutpat placerat diam, in tempus ipsum venenatis vitae. Curabitur vel nibh eget sem vulputate volutpat ac at enim.</p>
    <a class="learn">Learn More</a>
  </div>
  <div class="abs feature" style="left:726px">
    <div class="feature-head">
    <svg width="28" height="26" viewBox="0 0 28 26"><path d="M3 2 V23 H27" fill="none" stroke="#333" stroke-width="2.5"/><path d="M7 19 L12 10 L16 16 L23 5" fill="none" stroke="#333" stroke-width="2.5"/></svg>
    <h2>Increased Bottomline</h2></div>
    <p>Lorem ipsum dolor sit amet, consectetur adipiscing elit. Proin vitae magna eget neque commodo rutrum ut vel turpis. Integer a purus urna. Maecenas a laoreet sapien. Mauris volutpat placerat diam, in tempus ipsum venenatis vitae. Curabitur vel nibh eget sem vulputate volutpat ac at enim.</p>
    <a class="learn">Learn More</a>
  </div>
</section>

<footer class="abs footer">
  <div class="abs footer-brand">Quillmark</div>
  <div class="abs copyright">Copyright 2001-2013 Quillmark. Rights Reserved.</div>
  <div class="abs footer-links">People | Companies | SiteMap</div>
</footer>

<aside class="abs social-box">
  <div class="abs stay">Stay Connected</div>
  <div class="abs social-icons">
    <span aria-label="chatterbox"></span><span aria-label="peeper"></span><span aria-label="orbitnet+"></span><span aria-label="workLoop"></span>
  </div>
  <div class="abs share-row">
    <span>Lubię to!</span><span>42 ty</span><span>+1</span><span>1.3k</span><span>Post</span><span>5,852</span>
  </div>
</aside>

</body>
</html>
```